Asian Speciality Coffee label for brown valve bag. YUNNAN.

We are in need of a front and back coffee label for a brown paper valve bag.

Our brand is Lumo Brava. We source the finest and rarest varieties of coffee from the four corners of South East Asia that have been until now kept secret. Our selection has been cultivated by tribal communities and micro lot farmers who for generations have taken pride in organically producing truly amazing coffees. The result is coffee unlike any we have ever tasted before, truly showing how special Asian kapé can be. We believe every bean is precious which is why we ensure all our coffees are sourced ethically through direct trade, roasted by specialists and treated with utmost respect to fulfill our promise of serving you kapé that gives happiness in every cup.

The design of the label will encompass our Company Name logo and signature drinking buddha logo. We want a logo that stands out but at the sane time clearly displaying the finer details of the coffee, such as taste notes, variety etc.

The particular variety we want a label for is called YUNNAN.
Complete details of the coffee are found on our websitehttp://www.lumobrava-example.com/shop/yunnan

The front of the bag I would ideally like a picture of the farmer, of which I have provided on website or attached. Together with the name of the coffee and our company logo. Perhaps further details of the coffee can be found on the back. But would like to see creative input.

please look up our website to read more about us. www.lumobrava-example.com

Target Market(s)

Speciality Coffee

Requirements
Must have
• Company name logo Lumo Brava, Drinking Buddha stamp. Details about the coffee. Product name: Yunnan.
• Product details can be found here http://www.lumobrava-example.com/shop/yunnan
• or
• Origin: Yunnan Province, Southern China
• Variety: Arabica - Catimor
• Altitude Grown: 1100 - 1400 ft
• Farmer: Co-operative of micro lots
• Process: Fully Washed
• Yunnan’, in local dialect means ‘South of the Cloud’. The Yunnan province located in Southern China is graced with world renowned scenic beauty for its tranquil mountainous valleys. The name we chose for this coffee originated from the location of the coffee trees growing south of the Yunling Mountains (known to locals as Cloud Mountain).Our ‘Yunnan’ coffee is grown south of the Yunling in the rolling hills of Bao Shan and Kunming at an altitude of 1100 - 1400 meters. Pairing organic farming methods and top grade washing and sorting facilities have allowed the farms we work with to perfect their coffee to specialty grade quality. The result of their hard work and dedication to their harvest was evident to us from our first cup.
Should not have
• sticker label will be on a brown paper bag.

```html
<!DOCTYPE html>
<html lang="en">
<head>
<meta charset="utf-8">
<title>Lumo Brava – Yunnan coffee labels</title>
<link href="https://fonts.googleapis.com/css2?family=Oswald:wght@500;600&family=Roboto+Condensed:ital,wght@0,400;1,400&family=Courgette&display=swap" rel="stylesheet">
<style>
  :root {
    --backdrop: #e6d8bd;
    --kraft-light: #d7b985;
    --kraft: #c49f66;
    --kraft-dark: #9c7a48;
    --ink: #141210;
    --gold: #d9b271;
    --gold-deep: #a9823f;
    --cream: #f4ead7;
    --sepia-dark: #3b3226;
    --sepia-mid: #8a7556;
  }
  * { box-sizing: border-box; margin: 0; padding: 0; }
  html, body { width: 1200px; height: 900px; overflow: hidden; }
  body {
    background: var(--backdrop);
    font-family: "Roboto Condensed", "Arial Narrow", sans-serif;
    position: relative;
  }
  .brand-mark {
    position: absolute; left: 0; top: 150px; width: 1200px;
    text-align: center;
    font-family: "Oswald", "Arial Narrow", sans-serif;
    font-weight: 600; font-size: 76px; letter-spacing: 3px;
    color: var(--ink); line-height: 1;
  }
  .label {
    position: absolute; top: 378px; width: 300px; height: 440px;
    background: linear-gradient(180deg, var(--kraft-light), var(--kraft) 60%, var(--kraft-dark));
    overflow: hidden;
  }
  .label--front { left: 236px; }
  .label--back { left: 664px; }

  /* front */
  .farmer-photo {
    position: absolute; left: 0; top: 40px; width: 300px; height: 250px;
    background: linear-gradient(180deg, rgba(60,50,38,0) 0%, var(--sepia-mid) 35%, var(--sepia-dark) 100%);
  }
  .front-base { position: absolute; left: 0; top: 0; }
  .front-logo {
    position: absolute; left: 100px; top: 0; width: 100px; height: 86px;
    background: var(--ink); border: 2px solid var(--gold);
    display: flex; align-items: center; justify-content: center; text-align: center;
    font-family: "Oswald", sans-serif; font-weight: 600; font-size: 20px; line-height: 1.05;
    color: var(--gold); letter-spacing: 1px;
  }
  .stamp {
    position: absolute; border-radius: 50%;
    border: 3px solid var(--ink); background: var(--gold);
  }
  .label--front .stamp { left: 118px; top: 176px; width: 64px; height: 64px; }
  .product-name {
    position: absolute; left: 0; width: 300px; text-align: center;
    font-family: "Oswald", sans-serif; font-weight: 600; line-height: 1;
  }
  .label--front .product-name {
    top: 236px; font-size: 46px; color: var(--gold);
    -webkit-text-stroke: 1px var(--ink);
  }
  .variety {
    position: absolute; left: 0; top: 320px; width: 300px; text-align: center;
    font-family: "Courgette", cursive; font-size: 19px; color: var(--cream);
  }
  .front-story {
    position: absolute; left: 18px; top: 361px; width: 264px; text-align: center;
    font-style: italic; font-size: 9.4px; line-height: 1.2; color: var(--cream);
  }
  .net-weight {
    position: absolute; left: 0; top: 412px; width: 300px; text-align: center;
    font-family: "Oswald", sans-serif; font-weight: 500; font-size: 14px; color: var(--cream);
  }

  /* back */
  .label--back .stamp { left: 126px; top: 42px; width: 48px; height: 48px; background: var(--kraft-light); border-width: 2px; }
  .label--back .product-name { top: 102px; font-size: 36px; color: var(--ink); }
  .back-story {
    position: absolute; left: 22px; top: 168px; width: 256px; text-align: center;
    font-size: 8.2px; line-height: 1.18; color: var(--ink);
  }
  .back-story p + p { margin-top: 10px; }
  .bean-field {
    position: absolute; left: 0; top: 330px; width: 300px; height: 110px;
    background: linear-gradient(180deg, rgba(120,95,60,0), rgba(120,95,60,0.45));
  }
</style>
</head>
<body>
  <div class="brand-mark">Lumo Brava</div>

  <section class="label label--front" aria-label="Front label">
    <div class="farmer-photo" role="img" aria-label="Sepia photograph of a farmer raking coffee beans drying in the sun"></div>
    <svg class="front-base" width="300" height="440" viewBox="0 0 300 440" aria-hidden="true">
      <polygon points="0,270 300,238 300,440 0,440" fill="var(--ink)"/>
      <polygon points="0,270 300,238 300,243 0,275" fill="var(--gold-deep)"/>
    </svg>
    <div class="front-logo">Lumo<br>Brava</div>
    <div class="stamp" aria-hidden="true"></div>
    <h1 class="product-name">YUNNAN</h1>
    <div class="variety">Arabica - Catimor</div>
    <p class="front-story">Yunnan coffee is original from the location of the coffee trees growing south of the Yunling Mountains. The rising wave of specialty coffee sweeping China has allowed for locally sourced outstanding coffees to take centre stage and showcase their amazing quality.</p>
    <div class="net-weight">900 G</div>
  </section>

  <section class="label label--back" aria-label="Back label">
    <div class="bean-field" role="img" aria-label="Faded photograph of roasted coffee beans"></div>
    <div class="stamp" aria-hidden="true"></div>
    <h2 class="product-name">YUNNAN</h2>
    <div class="back-story">
      <p>‘Yunnan’, in local dialect means ‘South of the Cloud’. The Yunnan province located in Southern China is graced with world renowned scenic beauty for its tranquil mountainous valleys. The name we chose for this coffee originated from the location of the coffee trees growing south of the Yunling Mountains (known to locals as Cloud Mountain). The rising wave of specialty coffee sweeping China has allowed for locally sourced outstanding coffees to take centre stage and showcase their amazing quality.</p>
      <p>Our ‘Yunnan’ coffee is grown south of the Yunling in the rolling hills of Bao Shan and Kunming at an altitude of 1100 - 1400 meters. Pairing organic farming methods and top grade washing and sorting facilities have allowed the farms we work with to perfect their coffee to specialty grade quality. The result of their hard work and dedication to their harvest was evident to us from our first cup.</p>
      <p>From such a humble cherry grown in the hills of Yunnan, comes China’s finest coffee. Selected twice to be used as single origin coffee in the Regional Brewers Cup in 2013 and 2014, the farmers have truly cultivated coffee of world class quality. The cooperatives working with the farmers concentrate their efforts on water sustainability, organic fertilisers and education on organic farming techniques to ensure continual growth in the quality in coffee produced and life of the community.</p>
    </div>
  </section>
</body>
</html>
```